Torvel, Inc. new buisness cards - brand guide included

We need new business cards. SLEAK SIMPLE FINANCE. They must include a place for NAME, TITLE, CELL, OFFICE PHONE, EMAIL. they also must include our services across the bottom. AIR, OCEAN, FTL, LTL, EXPRESS. for reference this will be being handed to some of the most prestigious shipping companies in a america.

Target Market(s)

Finance and corporate

Contact Information for Business Card

We need new business cards. SLEAK SIMPLE FINANCE. They must include a place for NAME, TITLE, CELL, OFFICE PHONE, EMAIL. they also must include our services across the bottom. AIR, OCEAN, FTL, LTL, EXPRESS.

Requirements
Must have
• We need new business cards. SLEAK SIMPLE FINANCE. They must include a place for NAME, TITLE, CELL, OFFICE PHONE, EMAIL. they also must include our services across the bottom. AIR, OCEAN, FTL, LTL, EXPRESS.
Nice to have
• USE THE COLORS AND LOGO IN THE BRAND GUIDE :)

```html
<!DOCTYPE html>
<html lang="en">
<head>
<meta charset="UTF-8">
<title>Torvel, Inc. Business Card</title>
<link href="https://fonts.googleapis.com/css2?family=Tinos:wght@400;700&display=swap" rel="stylesheet">
<style>
  :root {
    --backdrop: #8a8b8f;
    --paper: #ffffff;
    --gold: #c2b28f;
    --gold-deep: #b3a27d;
    --gold-light: #d4c8ae;
    --ink: #262626;
    --icon: #b0a285;
  }
  * { margin: 0; padding: 0; box-sizing: border-box; }
  html, body { width: 900px; height: 1200px; overflow: hidden; }
  body {
    background: var(--backdrop);
    font-family: "Tinos", "Times New Roman", serif;
    position: relative;
  }
  .card {
    position: absolute;
    left: 134px;
    width: 633px;
    height: 362px;
  }
  .card-front { top: 213px; }
  .card-back { top: 627px; background: var(--paper); }

  .front-field {
    position: absolute;
    inset: 0;
    background: linear-gradient(100deg, var(--gold-deep) 0%, var(--gold) 45%, var(--gold-light) 100%);
  }
  .front-name {
    position: absolute;
    left: 0; right: 0;
    top: 151px;
    text-align: center;
    font-size: 56px;
    font-weight: 400;
    letter-spacing: 4px;
    color: #ffffff;
    line-height: 1;
  }

  .brand-name {
    position: absolute;
    left: 88px;
    top: 127px;
    width: 224px;
    height: 108px;
    display: flex;
    align-items: center;
    justify-content: center;
    font-size: 44px;
    font-weight: 400;
    letter-spacing: 3px;
    color: var(--gold);
  }
  .divider {
    position: absolute;
    left: 343px;
    top: 82px;
    width: 1px;
    height: 197px;
    background: var(--ink);
  }
  .contact {
    position: absolute;
    left: 370px;
    top: 78px;
    color: var(--ink);
  }
  .person-name { font-size: 23px; font-weight: 700; line-height: 1.1; }
  .person-title {
    font-size: 14px; font-weight: 700; color: var(--gold);
    letter-spacing: 1px; margin-top: 3px;
  }
  .address { font-size: 13.5px; line-height: 20px; margin-top: 10px; }
  .lines { list-style: none; margin-top: 10px; }
  .lines li {
    display: flex; align-items: center;
    font-size: 13.5px; letter-spacing: 1px;
    height: 24px;
  }
  .lines svg { width: 12px; height: 12px; margin-right: 6px; flex: none; }
  .services {
    position: absolute;
    left: 0; right: 0;
    top: 310px;
    text-align: center;
    font-size: 18px;
    font-weight: 700;
    letter-spacing: 1px;
    color: var(--ink);
  }
</style>
</head>
<body>
  <section class="card card-front">
    <div class="front-field" role="img" aria-label="Embossed repeating brand pattern on gold card stock"></div>
    <div class="front-name">TORVEL</div>
  </section>

  <section class="card card-back">
    <div class="brand-name">TORVEL</div>
    <div class="divider"></div>
    <div class="contact">
      <div class="person-name">Dorian Hale</div>
      <div class="person-title">CEO</div>
      <div class="address">2210 Linden Court Ste 140<br>Alder Bay, WA 98301</div>
      <ul class="lines">
        <li>
          <svg viewBox="0 0 12 12"><rect x="3" y="0.5" width="6" height="11" rx="1" fill="none" stroke="var(--icon)" stroke-width="1.2"/><circle cx="6" cy="9.6" r="0.7" fill="var(--icon)"/></svg>
          555-214-3087
        </li>
        <li>
          <svg viewBox="0 0 12 12"><path d="M2.5 1 L4.6 1 L5.4 3.6 L4.2 4.6 C4.9 6.1 5.9 7.1 7.4 7.8 L8.4 6.6 L11 7.4 L11 9.5 C11 10.3 10.3 11 9.5 11 C5 10.7 1.3 7 1 2.5 C1 1.7 1.7 1 2.5 1 Z" fill="var(--icon)"/></svg>
          555-308-6192
        </li>
        <li>
          <svg viewBox="0 0 12 12"><rect x="0.5" y="2.5" width="11" height="7.5" fill="var(--icon)"/><path d="M0.8 2.8 L6 7 L11.2 2.8" fill="none" stroke="#fff" stroke-width="1"/></svg>
          DH@torvelinc.com
        </li>
        <li>
          <svg viewBox="0 0 12 12"><circle cx="6" cy="6" r="5.2" fill="none" stroke="var(--icon)" stroke-width="1"/><ellipse cx="6" cy="6" rx="2.3" ry="5.2" fill="none" stroke="var(--icon)" stroke-width="0.9"/><line x1="0.8" y1="6" x2="11.2" y2="6" stroke="var(--icon)" stroke-width="0.9"/><line x1="1.6" y1="3.4" x2="10.4" y2="3.4" stroke="var(--icon)" stroke-width="0.8"/><line x1="1.6" y1="8.6" x2="10.4" y2="8.6" stroke="var(--icon)" stroke-width="0.8"/></svg>
          www.torvelinc.com
        </li>
      </ul>
    </div>
    <div class="services">AIR | OCEAN | FTL | LTL | EXPRESS.</div>
  </section>
</body>
</html>
```